Velmora - New coded website

Current website is around 5 years old and corrupted in some ways...
I would like to refresh the design and to create a new coded website based on the current content .
Please refer to :
www.velmora-sample.com.au

Coded - Design and coding required

```html
<!DOCTYPE html>
<html lang="en">
<head>
<meta charset="utf-8">
<title>Velmora – Odours Controlled Naturally</title>
<link href="https://fonts.googleapis.com/css2?family=Poppins:ital,wght@0,400;0,500;0,600;0,700;1,400&display=swap" rel="stylesheet">
<style>
:root{
  --green:#5cb343;
  --green-dark:#3f9a3a;
  --teal:#1a7d68;
  --navy:#1b3d6e;
  --navy-deep:#17365f;
  --ink:#3d3d3d;
  --muted:#6b6b6b;
  --light:#f4f4f4;
  --white:#ffffff;
}
*{box-sizing:border-box;margin:0;padding:0}
html,body{width:1200px;height:4348px;overflow:hidden}
body{position:relative;font-family:'Poppins',sans-serif;color:var(--ink);background:var(--white)}
.abs{position:absolute}
.btn{position:absolute;display:flex;align-items:center;justify-content:center;color:var(--white);font-weight:600;background:linear-gradient(90deg,var(--green),var(--teal));border-radius:999px;text-decoration:none}

/* hero */
.hero{left:0;top:0;width:1200px;height:620px;background:linear-gradient(180deg,#4e6a86 0%,#7f8f8a 40%,#6f7d5a 70%,#5b5a3c 100%)}
.brand{left:37px;top:33px;display:flex;align-items:center;gap:14px;color:var(--white);font-size:40px;font-weight:500}
.brand .dot{width:62px;height:62px;border-radius:50%;background:var(--green)}
.topnav{left:608px;top:56px;display:flex;align-items:center;gap:18px;color:var(--white);font-size:15px;font-weight:500}
.topnav span{display:flex;align-items:center;gap:8px}
.ic{width:26px;height:26px;border-radius:50%;background:var(--green);display:flex;align-items:center;justify-content:center}
.nav-quote{left:928px;top:47px;width:161px;height:46px;border-radius:6px;background:var(--green);font-size:15px}
.burger{left:1117px;top:57px;width:39px}
.burger i{display:block;height:4px;background:var(--green);margin-bottom:7px;border-radius:2px}
.hero-badge{left:101px;top:211px;width:304px;height:304px;border-radius:50%;background:linear-gradient(160deg,var(--green),var(--teal) 60%,var(--navy));display:flex;flex-direction:column;align-items:center;justify-content:center;color:var(--white);text-align:center}
.hero-badge h1{font-size:37px;line-height:42px;font-weight:600}
.hero-badge .btn{position:static;margin-top:14px;width:152px;height:34px;border-radius:8px;background:var(--green);font-size:14px}
.video-card{left:694px;top:510px;width:391px;height:212px;border-radius:50px;background:linear-gradient(180deg,#fbfcf7,#e3efd9);box-shadow:0 6px 18px rgba(0,0,0,.15);overflow:hidden}
.video-card .art{position:absolute;left:20px;top:60px;right:20px;bottom:20px;border-radius:10px;background:linear-gradient(180deg,#d4e8c4,#5eaa58 60%,#1f5d7a)}
.video-card .play{position:absolute;left:175px;top:85px;width:42px;height:42px;border-radius:50%;background:var(--navy);display:flex;align-items:center;justify-content:center}

/* products */
h2.title{position:absolute;left:0;width:1200px;text-align:center;font-weight:700;color:var(--navy)}
.product{position:absolute;top:881px;width:282px;height:312px}
.product .ph{height:225px}
.product .lbl{height:87px;display:flex;align-items:center;justify-content:center;text-align:center;color:var(--white);font-size:18px;font-weight:600;line-height:23px;background:linear-gradient(180deg,#6cbf3e,var(--green-dark))}
.product .lbl.alt{background:linear-gradient(135deg,var(--green),var(--navy))}

/* about */
.about{left:0;top:1291px;width:1200px;height:549px;background:var(--light)}
.about .kicker{left:154px;top:98px;font-size:21px;font-weight:600;color:var(--navy)}
.about h2{position:absolute;left:152px;top:124px;font-size:44px;font-weight:700;color:var(--navy)}
.about p{position:absolute;left:152px;top:186px;width:460px;font-size:13.5px;line-height:21.7px;color:var(--ink)}
.about p u{text-decoration:underline}
.about .btn{left:143px;top:360px;width:156px;height:51px;font-size:15px}
.about .circle{left:676px;top:90px;width:380px;height:380px;border-radius:50%;background:linear-gradient(135deg,#7a6658,#8e9a7f 45%,#cfc7a8 70%,#9aa19a)}

/* testimonial */
.testi{left:0;top:1840px;width:1200px;height:447px;background:linear-gradient(90deg,#4ea840,#2a8c5c 55%,var(--teal));color:var(--white);text-align:center}
.testi h3{position:absolute;left:0;width:1200px;top:112px;font-size:18px;font-weight:600}
.testi blockquote{position:absolute;left:198px;top:150px;width:804px;font-size:14.8px;line-height:24.4px;font-style:italic}
.testi .who{position:absolute;left:0;width:1200px;top:326px;font-size:16px;font-weight:700;line-height:18px}
.testi .who small{display:block;font-size:9.5px;font-weight:600}

/* gallery */
.g{position:absolute;border-radius:34px 34px 34px 0}
.view-all{left:544px;top:3015px;width:111px;height:37px;border-radius:4px 18px 4px 18px;font-size:14px}

/* clients */
.clients{left:0;top:3131px;width:1200px;height:329px;background:var(--light)}
.clients h2{position:absolute;left:0;width:1200px;top:78px;text-align:center;font-size:30px;font-weight:600;color:var(--navy)}
.tile{position:absolute;top:144px;width:165px;height:94px;background:var(--white);border-radius:4px;display:flex;align-items:center;justify-content:center;gap:8px;font-size:15px;font-weight:600;color:var(--navy)}
.tile .sq{width:16px;height:16px;border-radius:50%;background:var(--navy)}

/* contact */
.contact{left:0;top:3460px;width:1200px;height:517px;background:linear-gradient(180deg,#1e4478,var(--navy-deep))}
.contact h2{position:absolute;left:0;width:1200px;top:78px;text-align:center;font-size:44px;font-weight:700;color:var(--white)}
.field{position:absolute;background:var(--white);font-size:12px;color:#555;padding:16px 16px;display:flex;align-items:flex-start;gap:6px}
.submit{left:506px;top:3815px;width:188px;height:67px;font-size:17px;font-weight:700;background:linear-gradient(90deg,#4eb048,#2f9a3f)}

/* footer */
.f-brand{left:132px;top:4150px;color:var(--navy);font-size:40px;font-weight:500;display:flex;align-items:center;gap:10px}
.f-brand .dot{width:34px;height:34px;border-radius:50%;background:var(--green)}
.f-head{position:absolute;top:4040px;font-size:16px;font-weight:600;color:#333}
.f-links{position:absolute;left:373px;top:4094px;font-size:11.5px;line-height:26.5px;color:#444;list-style:none}
.f-row{position:absolute;left:567px;display:flex;align-items:center;gap:16px;font-size:12px;color:#333;line-height:15px}
.f-row .sq{width:34px;height:34px;background:var(--green);display:flex;align-items:center;justify-content:center;flex:none}
.news-text{position:absolute;left:822px;top:4092px;width:240px;font-size:11px;line-height:13px;color:#444}
.news-input{position:absolute;left:824px;top:4144px;width:231px;height:42px;background:#f1f1f1;display:flex;align-items:center;padding-left:16px;font-size:12px;color:#333}
.news-input .go{position:absolute;right:0;top:0;width:44px;height:42px;background:var(--green);display:flex;align-items:center;justify-content:center}
.rule{left:118px;top:4279px;width:939px;height:1px;background:#cfcfcf}
.copy{position:absolute;left:0;width:1200px;top:4306px;text-align:center;font-size:12px;color:#555}
</style>
</head>
<body>

<!-- hero -->
<section class="abs hero" role="img" aria-label="Photo of green biofilter tanks at a treatment site under a cloudy sky"></section>
<div class="abs brand"><span class="dot"></span>Velmora</div>
<nav class="abs topnav">
  <span><i class="ic"><svg width="13" height="13" viewBox="0 0 24 24"><path fill="#fff" d="M6.6 10.8a15 15 0 0 0 6.6 6.6l2.2-2.2a1 1 0 0 1 1-.25 11.4 11.4 0 0 0 3.6.57 1 1 0 0 1 1 1V20a1 1 0 0 1-1 1A17 17 0 0 1 3 4a1 1 0 0 1 1-1h3.5a1 1 0 0 1 1 1c0 1.25.2 2.45.57 3.57a1 1 0 0 1-.25 1z"/></svg></i>+61 (08) 5550 1234</span>
  <span><i class="ic"><svg width="13" height="13" viewBox="0 0 24 24"><path fill="#fff" d="M3 5h18v14H3z"/><path d="M3 6l9 7 9-7" stroke="#5cb343" stroke-width="2" fill="none"/></svg></i>Email Us</span>
</nav>
<a class="btn nav-quote">Request a Quote</a>
<div class="abs burger"><i></i><i></i><i></i></div>
<div class="abs hero-badge">
  <h1>Odours<br>Controlled<br>Naturally</h1>
  <a class="btn">Request a Quote</a>
</div>
<div class="abs video-card">
  <div class="art" role="img" aria-label="Illustration of biofilter units among trees and hills"></div>
  <div class="play"><svg width="16" height="16" viewBox="0 0 16 16"><path d="M4 2l10 6-10 6z" fill="#fff"/></svg></div>
</div>

<!-- products -->
<h2 class="title" style="top:800px;font-size:37px">Our Products</h2>
<article class="product" style="left:150px">
  <div class="ph" role="img" aria-label="Above ground odour vent tanks behind a fence" style="background:linear-gradient(160deg,#9b6e55,#5d5a4a 50%,#8b9a7a)"></div>
  <div class="lbl">Above Ground:<br>VelVent SPSV</div>
</article>
<article class="product" style="left:459px">
  <div class="ph" role="img" aria-label="Below ground vent along a grassed verge" style="background:linear-gradient(180deg,#c9ccc7,#8c8d88 45%,#6a8a4a)"></div>
  <div class="lbl alt">Below Ground:<br>VelVent MHV</div>
</article>
<article class="product" style="left:768px">
  <div class="ph" role="img" aria-label="Carbon filter vessels on a concrete pad" style="background:linear-gradient(180deg,#b9cbe0,#7d8f6a 50%,#a9a89c)"></div>
  <div class="lbl">Final Treatment:<br>VelCarb</div>
</article>

<!-- about -->
<section class="abs about">
  <div class="abs kicker">Odour Control Solutions</div>
  <h2>About Velmora</h2>
  <p>Velmora uses sustainable biotechnology to resolve odour and <u>corrosion</u> problems in a highly efficient, environmentally friendly and cost-effective manner. Our, products, the VelVent series of biofilters have been specifically engineered to overcome issues traditionally associated with biofiltration, such as bed compaction and uneven moisture levels, and our patented design achieves a removal rate of up to 99.9% per stage of treatment.</p>
  <a class="btn">Request a Quote</a>
  <div class="abs circle" role="img" aria-label="Photo of a biofilter installation with yellow access stairs"></div>
</section>

<!-- testimonial -->
<section class="abs testi">
  <h3>As soon as the system was started, the smell disappeared!</h3>
  <blockquote>"The Velmora team promised to stop the odour from our smelly neighbor and they delivered- in spades! As soon as the system was started, the smell disappeared. The system is well designed, very professionally installed and the beauty of it is, apart from a constantly running fan, it is bacteria doing the heavy lifting, so it is very environmentally friendly. We lived with the smell for 3 three years which could be extremely frustrating and unpleasant. Now, the problem is solved and we can have BBQs again. We are happy and our neighbours have noticed the odour is gone. Thank you!"</blockquote>
  <div class="who">Sam Ridley<small>Nearby resident to Elm Road Wastewater Pump Station</small></div>
</section>

<!-- gallery -->
<h2 class="title" style="top:2378px;font-size:50px">Our Gallery</h2>
<div class="g" role="img" aria-label="Aerial view of treatment ponds" style="left:150px;top:2470px;width:284px;height:241px;background:linear-gradient(180deg,#8ca6c2,#5b6f58 45%,#7f8a6b)"></div>
<div class="g" role="img" aria-label="Tanks beside a house" style="left:458px;top:2470px;width:283px;height:295px;background:linear-gradient(180deg,#b6c7df,#9a8f80 45%,#8b9a72)"></div>
<div class="g" role="img" aria-label="Two green tanks among trees" style="left:766px;top:2470px;width:284px;height:243px;background:linear-gradient(180deg,#5f8a4a,#8da273 50%,#777a6a)"></div>
<div class="g" role="img" aria-label="Biofilter with yellow stairs" style="left:150px;top:2731px;width:284px;height:242px;background:linear-gradient(160deg,#8a6a58,#8d9a80 50%,#b8b39a)"></div>
<div class="g" role="img" aria-label="Green tank between gum trees" style="left:458px;top:2787px;width:283px;height:186px;background:linear-gradient(180deg,#6d9a55,#9aa873 50%,#4c6a3c)"></div>
<div class="g" role="img" aria-label="Biofilter seen from above" style="left:766px;top:2729px;width:284px;height:244px;background:linear-gradient(160deg,#7c6658,#a8ad9a 50%,#c9c7b8)"></div>
<a class="btn view-all">View All</a>

<!-- clients -->
<section class="abs clients">
  <h2>Our Happy Clients</h2>
  <div class="tile" style="left:154px"><span class="sq"></span>Coastline City</div>
  <div class="tile" style="left:336px"><span class="sq"></span>Westvale Water</div>
  <div class="tile" style="left:518px"><span class="sq"></span>Northreach Govt</div>
  <div class="tile" style="left:699px"><span class="sq"></span>Riverbend Water</div>
  <div class="tile" style="left:881px"><span class="sq"></span>Harbour City</div>
</section>

<!-- contact -->
<section class="abs contact">
  <h2>Get in Contact</h2>
</section>
<div class="field" style="left:167px;top:3634px;width:279px;height:47px">&#9786; Name:</div>
<div class="field" style="left:461px;top:3634px;width:278px;height:47px">&#9993; Email:</div>
<div class="field" style="left:755px;top:3634px;width:278px;height:47px">&#9742; Phone:</div>
<div class="field" style="left:167px;top:3697px;width:866px;height:152px">&#9675; Message:</div>
<a class="btn submit">SUBMIT NOW</a>

<!-- footer -->
<div class="abs f-brand"><span class="dot"></span>Velmora</div>
<div class="f-head" style="left:373px">Links</div>
<ul class="f-links">
  <li>Odour Control Products</li>
  <li>How Biofiltration Works</li>
  <li>Odour Control by Industry</li>
  <li>Past Projects</li>
  <li>About Us</li>
</ul>
<div class="f-head" style="left:574px">Contact Us</div>
<div class="f-row" style="top:4099px"><span class="sq"><svg width="14" height="16" viewBox="0 0 24 24"><path fill="#fff" d="M12 2a7 7 0 0 0-7 7c0 5 7 13 7 13s7-8 7-13a7 7 0 0 0-7-7zm0 9.5A2.5 2.5 0 1 1 12 6.5a2.5 2.5 0 0 1 0 5z"/></svg></span><span style="font-size:11px">12 Sample Way,<br>Northvale WA 6000, Australia</span></div>
<div class="f-row" style="top:4161px"><span class="sq"><svg width="14" height="14" viewBox="0 0 24 24"><path fill="#fff" d="M6.6 10.8a15 15 0 0 0 6.6 6.6l2.2-2.2a1 1 0 0 1 1-.25 11.4 11.4 0 0 0 3.6.57 1 1 0 0 1 1 1V20a1 1 0 0 1-1 1A17 17 0 0 1 3 4a1 1 0 0 1 1-1h3.5a1 1 0 0 1 1 1c0 1.25.2 2.45.57 3.57a1 1 0 0 1-.25 1z"/></svg></span><span style="font-size:14px">+61 (08) 5550 1234</span></div>
<div class="f-row" style="top:4212px"><span class="sq"><span style="width:12px;height:12px;background:#fff;display:block"></span></span><span style="font-size:14px">Linkup</span></div>
<div class="f-head" style="left:822px">Newsletter Sign up</div>
<p class="news-text">Lorem ipsum dolor sit amelor conse ctet ur adipiscilorem ipsumilt,</p>
<div class="news-input">Email<span class="go"><svg width="28" height="14" viewBox="0 0 28 14"><path d="M1 7h24M19 1l6 6-6 6" stroke="#fff" stroke-width="1.6" fill="none"/></svg></span></div>
<div class="abs rule"></div>
<p class="copy">© 2023 All Rights Reserved.Terms &amp; Conditions Privacy Policy</p>

</body>
</html>
```